I need cover art for my first album

I am releasing my first album and I need cover art for the CD  packaging. The art would also be used in Tunevale and other streaming services. The music is dark, experimental electronic music. It includes lots of soundscapes with industrial, metallic sounds. Similar artists include Grevhald and Ivor Pennick. The album's concept is inspired by the loneliness and inherent dangers of long-term space travel and living alone in cold, distant space stations.
You can hear a rough cut of one of the tracks for the album at https://echoloft.net/kelvorant/tidegrove.

Colors
Designer to choose colors to be used in the design.
Requirements
Must have
- The design should be abstract and minimalist but not only grayscale. I would like to see color used in ways that convey feelings. Provide a sense of movement.
Should not have
- No images of moons or planets. Please don't be literal with the "space" theme.

```html
<!DOCTYPE html>
<html lang="en">
<head>
<meta charset="utf-8">
<title>Sunken Into Nightfield — Kelvorant</title>
<link rel="stylesheet" href="https://fonts.googleapis.com/css2?family=Marcellus&family=Michroma&display=swap">
<style>
  :root {
    --void: #05030d;
    --deep-violet: #1c1147;
    --violet: #5b46d6;
    --glow-violet: #8f7cf5;
    --title-ink: #b8b0fb;
    --artist-ink: #ddd8ff;
  }
  html, body {
    margin: 0;
    padding: 0;
    width: 1200px;
    height: 1195px;
    overflow: hidden;
    background: var(--void);
  }
  .cover {
    position: relative;
    width: 1200px;
    height: 1195px;
    overflow: hidden;
    background: var(--void);
  }
  .cover-artwork {
    position: absolute;
    inset: 0;
    background:
      radial-gradient(ellipse 380px 500px at 900px 640px, var(--glow-violet) 0%, var(--violet) 45%, transparent 78%),
      radial-gradient(ellipse 320px 400px at 140px 920px, var(--violet) 0%, var(--deep-violet) 55%, transparent 85%),
      radial-gradient(ellipse 150px 400px at 400px 300px, var(--violet) 0%, var(--deep-violet) 55%, transparent 85%),
      radial-gradient(ellipse 130px 280px at 760px 110px, var(--violet) 0%, transparent 80%),
      linear-gradient(180deg, var(--deep-violet) 0%, var(--void) 60%, var(--void) 100%);
  }
  .cover-title {
    position: absolute;
    right: 318px;
    top: 762px;
    margin: 0;
    text-align: right;
    font-family: "Marcellus", serif;
    font-weight: 400;
    font-size: 80px;
    line-height: 84px;
    letter-spacing: 3px;
    color: var(--title-ink);
    text-transform: uppercase;
    white-space: nowrap;
  }
  .cover-title span { display: block; }
  .cover-artist {
    position: absolute;
    left: 425px;
    top: 966px;
    margin: 0;
    font-family: "Michroma", sans-serif;
    font-weight: 400;
    font-size: 26px;
    line-height: 40px;
    letter-spacing: 18px;
    color: var(--artist-ink);
    text-transform: uppercase;
    white-space: nowrap;
    -webkit-text-stroke: 1.6px var(--artist-ink);
  }
</style>
</head>
<body>
  <main class="cover">
    <div class="cover-artwork" role="img" aria-label="Violet-tinted close-up photograph of two pale, rounded hanging forms suspended by thin strings against darkness"></div>
    <h1 class="cover-title">
      <span>Sunken Into</span>
      <span>Nightfield</span>
    </h1>
    <p class="cover-artist">Kelvorant</p>
  </main>
</body>
</html>
```